Talvero

I'd like new business card design options. I'll need to provide updated contact info although after the deign is complete. We are in IT, specifically in the data backup, archiving and disaster recovery verticals.

Business

```html
<!DOCTYPE html>
<html lang="en">
<head>
<meta charset="utf-8">
<title>Talvero business card</title>
<link href="https://fonts.googleapis.com/css2?family=Didact+Gothic&display=swap" rel="stylesheet">
<style>
  :root {
    --page-bg: #fde9e8;
    --card-dark: #212121;
    --card-blue: #39a5da;
    --brand-blue: #2d5fae;
    --tagline-blue: #3f8fd0;
    --banner-white: #ffffff;
    --fold-grey: #cfcfcf;
    --ink: #111111;
    --light-text: #ffffff;
  }
  * { margin: 0; padding: 0; box-sizing: border-box; }
  html, body {
    width: 1200px; height: 1200px; overflow: hidden;
    background: var(--page-bg);
    font-family: "Didact Gothic", "Century Gothic", sans-serif;
  }
  .business-card {
    position: absolute; left: 127px; top: 330px;
    width: 946px; height: 541px;
    background: var(--card-blue);
    overflow: hidden;
  }
  .card-art { position: absolute; inset: 0; }
  .brand-name, .brand-tagline, .person-name, .person-title, .contact-line {
    position: absolute; white-space: nowrap;
  }
  .brand-name {
    left: 137px; top: 253px;
    font-size: 40px; letter-spacing: 7px; color: var(--brand-blue);
  }
  .brand-tagline {
    left: 138px; top: 303px;
    font-size: 18px; letter-spacing: 1.5px; color: var(--tagline-blue);
  }
  .person-name {
    right: 55px; top: 86px;
    font-size: 32px; color: var(--ink); letter-spacing: -0.5px; word-spacing: -3px;
  }
  .person-title {
    right: 55px; top: 160px;
    font-size: 31px; color: var(--light-text);
  }
  .contact-line { left: 578px; color: var(--ink); font-size: 23px; line-height: 32px; }
  .contact-email { top: 219px; font-size: 22px; }
  .contact-address { top: 280px; }
  .contact-phone { top: 374px; }
  .contact-web { top: 472px; font-size: 22px; }
</style>
</head>
<body>
  <div class="business-card">
    <svg class="card-art" width="946" height="541" viewBox="0 0 946 541" aria-hidden="true">
      <rect class="dark-panel" x="0" y="0" width="442" height="541" fill="var(--card-dark)"/>
      <polygon class="banner-fold" points="383,149 483,149 483,198 442,180" fill="var(--fold-grey)"/>
      <rect class="divider-line" x="459" y="0" width="4" height="541" fill="var(--card-dark)"/>
      <rect class="divider-line" x="478" y="0" width="5" height="541" fill="var(--card-dark)"/>
      <rect class="name-banner" x="383" y="58" width="563" height="91" fill="var(--banner-white)"/>
      <circle class="brand-dot" cx="83" cy="284" r="35" fill="var(--tagline-blue)"/>

      <g class="icon-mail" fill="none" stroke-width="2">
        <rect x="530" y="219" width="38" height="25" fill="#fff" stroke="none"/>
        <polyline points="530,219 549,234 568,219" stroke="var(--card-blue)"/>
        <line x1="530" y1="244" x2="544" y2="231" stroke="var(--card-blue)"/>
        <line x1="568" y1="244" x2="554" y2="231" stroke="var(--card-blue)"/>
      </g>
      <path class="icon-pin" fill="#fff" fill-rule="evenodd"
        d="M549 272 a15 15 0 0 1 15 15 c0 11 -15 27 -15 27 s-15 -16 -15 -27 a15 15 0 0 1 15 -15 z M549 281 a6 6 0 1 0 0.1 0 z"/>
      <path class="icon-phone" fill="#fff"
        d="M537 364 l8 -4 l7 12 l-6 4 c2 6 6 11 11 15 l5 -5 l11 8 l-4 7 c-19 -3 -34 -20 -32 -37 z"/>
      <g class="icon-web">
        <circle cx="549" cy="483" r="17" fill="#fff"/>
        <circle cx="549" cy="483" r="13" fill="none" stroke="var(--card-blue)" stroke-width="2"/>
        <line x1="536" y1="483" x2="562" y2="483" stroke="var(--card-blue)" stroke-width="2"/>
        <ellipse cx="549" cy="483" rx="6" ry="13" fill="none" stroke="var(--card-blue)" stroke-width="2"/>
      </g>
    </svg>

    <div class="brand-name">TALVERO</div>
    <div class="brand-tagline">Data Backup Specialists</div>

    <div class="person-name">DANIEL R. WHITCOMBE, Ph.D</div>
    <div class="person-title">PRESIDENT, CTO</div>

    <div class="contact-line contact-email">daniel.whitcombe@talvero.com</div>
    <div class="contact-line contact-address">274 North Alder Avenue<br>Brookfield, Ohio 44403</div>
    <div class="contact-line contact-phone">800.555.0142<br>Fax:928.555.0187</div>
    <div class="contact-line contact-web">www.talvero.com</div>
  </div>
</body>
</html>
```